Wohnungsbaugenossenschaft sucht Webdesign
Zielgruppe
es geht um eine Wohnungsbaugenossenschaft, die Wohnungen an unterschiedlichen Standorten vermietet. Die Webseite soll die WBG präsentieren. Einerseits sollen die Mieter über 'Laufendes' informiert werden, andereseits sollen aktuelle Mietangebote mittels externen Link für potentielle Mieter angezeigt werden.
Aufgabenstellung
Logo, siehe Dateiupload, die Seite muss aber nicht unbedingt 'grün' sein. Diverse Fotos siehe Dateiupload (müssen nicht alle verwendet werden). Texte siehe jetzige Webseite, es können auch LoremIpsum verwendet werden.
Es soll nur die Startseite gelayoutet werden.

```html
<!DOCTYPE html>
<html lang="de">
<head>
<meta charset="utf-8">
<title>WG Lindenhof eG – Startseite</title>
<link rel="stylesheet" href="https://fonts.googleapis.com/css2?family=Fira+Sans+Condensed:wght@300;400;500&family=Fira+Sans:wght@300;400&family=Tinos:wght@400;700&family=Raleway:wght@400;700&display=swap">
<style>
:root{
  --green:#76a82a;
  --green-dark:#2e8a35;
  --ink:#222;
  --text:#555;
  --tile:#5b5b5b;
  --bg-soft:#eef0f2;
  --bar:#9ba8b8;
  --footer:#98a4b4;
  --white:#fff;
}
*{box-sizing:border-box;margin:0;padding:0}
html,body{width:1200px;height:2335px;overflow:hidden}
body{position:relative;background:var(--white);font-family:"Fira Sans Condensed",sans-serif;color:var(--text)}
.abs{position:absolute}
.header{left:0;top:0;width:1200px;height:74px;background:#e6e9ec}
.brand{left:101px;top:0;width:201px;height:124px;background:var(--white);z-index:3;display:flex;align-items:center;justify-content:center;gap:8px;font-weight:500;font-size:22px;color:var(--green-dark);white-space:nowrap}
.brand .sq{width:14px;height:14px;background:var(--green-dark)}
.nav{right:50px;top:24px;display:flex;align-items:center;font-size:12px;letter-spacing:1px;color:#444}
.nav span{padding:0 12px}
.nav .sep{padding:0}
.nav .active{color:var(--green-dark);font-weight:500}
.nav .phone{width:28px;height:28px;border-radius:50%;background:var(--green-dark);margin-left:10px;padding:0;display:flex;align-items:center;justify-content:center}
.hero{left:0;top:74px;width:1200px;height:399px;background:linear-gradient(100deg,#8a8f7c 0%,#c9bca4 30%,#b7c0c4 55%,#8fb070 80%,#79a347 100%)}
.hero-box{left:757px;top:179px;width:443px;height:169px;background:rgba(110,110,110,.78);padding:20px 0 0 43px;color:var(--white)}
.hero-box h1{font-family:Tinos,serif;font-weight:700;font-size:38px;letter-spacing:1px;line-height:1}
.hero-box p{font-family:"Fira Sans",sans-serif;font-style:italic;font-weight:300;font-size:30px;margin-top:4px}
.btn{display:inline-flex;align-items:center;justify-content:center;background:var(--green);color:var(--white);font-size:16px;letter-spacing:.5px}
.hero-box .btn{margin-top:12px;width:227px;height:35px}
.tile{top:448px;width:228px;height:185px}
.tile .img{height:146px}
.tile .label{height:39px;background:var(--tile);color:var(--white);font-size:18px;display:flex;align-items:center;justify-content:center;letter-spacing:.5px}
.kicker{color:var(--green-dark);font-size:18px;letter-spacing:.5px}
.title{font-family:Tinos,serif;color:var(--ink);font-size:30px;letter-spacing:3px;line-height:1.2;font-weight:400}
.welcome{left:104px;top:698px;width:530px}
.welcome .title{margin-top:6px}
.welcome p{font-size:16.5px;line-height:1.2;margin-top:20px;color:#555}
.sign{left:104px;top:962px;width:306px;height:22px;background:linear-gradient(90deg,#dfe3e7,#f4f5f7 80%,rgba(255,255,255,0))}
.team{left:653px;top:670px;width:435px;height:357px;background:linear-gradient(180deg,#fff 0%,#f3ebe4 22%,#d8c2b0 40%,#8a98b8 62%,#3d4d78 82%,#2c3a62 100%)}
.offers{left:0;top:1027px;width:1200px;height:400px;background:var(--bg-soft)}
.card{top:1138px;width:235px;height:194px}
.card .img{height:157px;background:linear-gradient(#5d8fc9,#a9b59a 60%,#7c8f54)}
.card .label{height:37px;background:var(--tile);color:var(--white);font-size:15.5px;display:flex;align-items:center;justify-content:center}
.locations{left:664px;top:1136px;width:422px;list-style:none}
.locations li{height:29px;display:flex;align-items:center;padding-left:6px;font-size:16px;color:#444}
.locations li.shade{background:var(--bar);color:var(--white)}
.locations svg{margin-right:6px}
.side{left:1146px;top:886px;width:54px;height:231px}
.side .up{height:50px;background:#4f4f4f;display:flex;align-items:center;justify-content:center}
.side .tab{height:131px;background:#5b5b5b;color:var(--white);writing-mode:vertical-rl;display:flex;align-items:center;justify-content:center;font-size:18px;letter-spacing:.5px}
.side .mail{height:50px;background:var(--green);display:flex;align-items:center;justify-content:center}
.center{left:0;width:1200px;text-align:center}
.news{top:1548px;width:302px}
.news .img{height:196px;position:relative}
.news .badge{position:absolute;right:0;top:0;width:43px;height:44px;background:var(--green);color:var(--white);font-size:13px;line-height:1.1;display:flex;flex-direction:column;align-items:center;justify-content:center}
.news h3{font-weight:400;color:var(--green-dark);font-size:19px;margin-top:8px}
.news p{font-size:12.5px;line-height:1.25;margin-top:6px;color:#555}
.news .more{display:inline-block;margin-top:8px;border:1px solid #777;font-size:9.5px;padding:6px 7px;letter-spacing:.5px;color:#555}
.contact{left:0;top:1890px;width:1200px;height:352px;background:var(--bg-soft)}
.intro{left:101px;top:1935px;width:400px}
.intro p{font-size:17px;line-height:1.25;margin-top:8px;color:#555}
.brand-small{left:101px;top:2050px;width:168px;height:70px;display:flex;align-items:center;gap:7px;font-weight:500;font-size:16px;color:var(--green-dark);white-space:nowrap}
.brand-small .sq{width:11px;height:11px;background:var(--green-dark)}
.addr{left:275px;top:2040px;font-size:12.5px;line-height:1.25;color:#555}
.addr div{display:flex;gap:6px;margin-bottom:6px}
.hours{left:476px;top:2040px;height:92px;border-left:1px solid var(--green);padding-left:18px;font-size:12.5px;line-height:1.3;color:#555}
.hours .h{color:var(--green-dark);display:flex;gap:5px;align-items:center;margin-bottom:6px}
.form{left:718px;top:1935px;width:400px}
.form h2{font-family:Tinos,serif;font-weight:400;font-size:34px;letter-spacing:4px;color:var(--ink)}
.field label{display:block;font-size:10px;color:#666;margin:12px 0 6px 3px}
.field .input{height:30px;background:var(--white)}
.note{font-size:7px;color:#555;line-height:1.5;margin-top:14px}
.send{left:1022px;top:2162px;width:94px;height:25px;font-size:13px}
.footer{left:0;top:2242px;width:1200px;height:93px;background:var(--footer);color:var(--white);font-family:Raleway,sans-serif;text-align:center}
.footer .links{margin-top:27px;font-size:13.5px}
.footer .links b{font-weight:700}
.footer .copy{margin-top:8px;font-size:13px}
</style>
</head>
<body>
<header class="abs header"></header>
<div class="abs brand"><span class="sq"></span>WG Lindenhof eG</div>
<nav class="abs nav">
  <span class="active">STARTSEITE</span><span class="sep">|</span>
  <span>ÜBER UNS</span><span class="sep">|</span>
  <span>AKTUELLE MIETANGEBOTE</span><span class="sep">|</span>
  <span>NEWS</span><span class="sep">|</span>
  <span>OBJEKTSTANDORTE</span><span class="sep">|</span>
  <span>NOTDIENST</span><span class="sep">|</span>
  <span>KONTAKT</span>
  <span class="phone"><svg width="14" height="14" viewBox="0 0 24 24"><path fill="#fff" d="M6.6 10.8a15 15 0 0 0 6.6 6.6l2.2-2.2a1 1 0 0 1 1-.25 11 11 0 0 0 3.6.6 1 1 0 0 1 1 1V20a1 1 0 0 1-1 1A17 17 0 0 1 3 4a1 1 0 0 1 1-1h3.5a1 1 0 0 1 1 1 11 11 0 0 0 .6 3.6 1 1 0 0 1-.25 1z"/></svg></span>
</nav>

<div class="abs hero" role="img" aria-label="Foto: lachendes Paar vor einem Haus auf grüner Wiese"></div>
<div class="abs hero-box">
  <h1>WOHNEN &amp; LEBEN</h1>
  <p>in Annaberg-Buchholz</p>
  <span class="btn">JETZT TERMIN VEREINBAREN</span>
</div>

<div class="abs tile" style="left:99px"><div class="img" role="img" aria-label="Foto: Mehrfamilienhaus im Grünen" style="background:linear-gradient(#7aa0cc,#c9cdc6 55%,#5f7d3c)"></div><div class="label">STANDORTE</div></div>
<div class="abs tile" style="left:363px"><div class="img" role="img" aria-label="Foto: Frau hält Wohnungsschlüssel" style="background:linear-gradient(120deg,#e8e4df,#c7a58a 60%,#9a8c94)"></div><div class="label">MIETANGEBOTE</div></div>
<div class="abs tile" style="left:628px"><div class="img" role="img" aria-label="Bild: zerrissenes Papier mit Schriftzug Zimmer frei" style="background:linear-gradient(#f3f3f3,#dcdcdc)"></div><div class="label">GÄSTEWOHNUNG</div></div>
<div class="abs tile" style="left:891px"><div class="img" role="img" aria-label="Foto: Sonnenuntergang über der Landschaft des Erzgebirges" style="background:linear-gradient(#5c6f8a,#d9a44a 55%,#6d8b2c)"></div><div class="label">TOURISMUS</div></div>

<section class="abs welcome">
  <div class="kicker">HERZLICH WILLKOMMEN</div>
  <h2 class="title">Ihre Wohnungsgenossenschaft<br>Lindenhof eG</h2>
  <p>Wir sind seit 1926 eine eingetragene Genossenschaft und verwalten zur Zeit ca. 456 Wohneinheiten. Neben Mehrfamilienhäusern verwalten wir auch Ein- und Zweifamilienhäuser. Alle Wohnungsstandorte sind rund um das malerische Annaberg gelegen. Die ganze Region gehört zum wunderschönen Erzgebirge.</p>
  <p>Lassen auch Sie sich von dieser schönen Wohngegend verzaubern.</p>
</section>
<div class="abs sign" role="img" aria-label="Handschriftzug: Ihr Team freut sich auf Sie"></div>
<div class="abs team" role="img" aria-label="Foto: jubelnde Gruppe junger Menschen mit erhobenem Daumen"></div>

<section class="abs offers"></section>
<div class="abs" style="left:103px;top:1056px">
  <div class="kicker">AKTUELLE MIETANGEBOTE</div>
  <h2 class="title" style="margin-top:2px">Wählen Sie Ihr Neues Zuhause</h2>
</div>
<div class="abs card" style="left:107px"><div class="img" role="img" aria-label="Foto: mehrstöckiges Wohnhaus"></div><div class="label">Birkenweg 15 und 17</div></div>
<div class="abs card" style="left:367px"><div class="img" role="img" aria-label="Foto: Wohnhaus mit Satteldach"></div><div class="label">Ahornstr. 2 | 09000 Talheim</div></div>
<span class="abs btn" style="left:375px;top:1350px;width:227px;height:36px">AKTUELLE MIETANGEBOTE</span>

<div class="abs" style="left:667px;top:1053px">
  <div class="kicker">UNSERE WOHNUNGEN / GEBÄUDE</div>
  <h2 class="title" style="margin-top:2px">Objektstandorte</h2>
</div>
<ul class="abs locations">
  <li class="shade"><svg width="8" height="11" viewBox="0 0 8 11"><path d="M1 1l5 4.5L1 10" stroke="currentColor" stroke-width="2" fill="none"/></svg>Annaberg- Buchholz</li>
  <li><svg width="8" height="11" viewBox="0 0 8 11"><path d="M1 1l5 4.5L1 10" stroke="currentColor" stroke-width="2" fill="none"/></svg>Cunersdorf</li>
  <li class="shade"><svg width="8" height="11" viewBox="0 0 8 11"><path d="M1 1l5 4.5L1 10" stroke="currentColor" stroke-width="2" fill="none"/></svg>Sehma</li>
  <li><svg width="8" height="11" viewBox="0 0 8 11"><path d="M1 1l5 4.5L1 10" stroke="currentColor" stroke-width="2" fill="none"/></svg>Schlettau</li>
  <li class="shade"><svg width="8" height="11" viewBox="0 0 8 11"><path d="M1 1l5 4.5L1 10" stroke="currentColor" stroke-width="2" fill="none"/></svg>Scheibenberg</li>
  <li><svg width="8" height="11" viewBox="0 0 8 11"><path d="M1 1l5 4.5L1 10" stroke="currentColor" stroke-width="2" fill="none"/></svg>Bärenstein und Geye</li>
</ul>
<span class="abs btn" style="left:907px;top:1350px;width:179px;height:36px">ZU DEN GEBÄUDEN</span>

<aside class="abs side">
  <div class="up"><svg width="24" height="14" viewBox="0 0 24 14"><path d="M1 13L12 2l11 11" stroke="#ddd" stroke-width="1.5" fill="none"/></svg></div>
  <div class="tab">MIETANGEBOTE</div>
  <div class="mail"><svg width="26" height="18" viewBox="0 0 26 18"><rect x="1" y="1" width="24" height="16" fill="#fff"/><path d="M1 1l12 9 12-9" stroke="#76a82a" stroke-width="1.5" fill="none"/></svg></div>
</aside>

<div class="abs center" style="top:1459px">
  <div class="kicker">BLEIBEN SIE AUF DEM LAUFENDEN</div>
  <h2 class="title" style="margin-top:2px">News für Mieter</h2>
</div>
<article class="abs news" style="left:102px"><div class="img" role="img" aria-label="Foto: glückliche Familie mit Kindern" style="background:linear-gradient(120deg,#d9dde0,#b38a6a 50%,#7c8fa6)"><div class="badge">APR<span>19</span></div></div><h3>Überschrift</h3><p>Lorem ipsum dolor sit amet, consetetur sadipscing elitr, sed diam nonumy...</p><span class="more">WEITER LESEN</span></article>
<article class="abs news" style="left:454px"><div class="img" role="img" aria-label="Visualisierung: Terrasse mit Garten vor Wohnanlage" style="background:linear-gradient(#8c8f88,#c9c8c0 40%,#6d8f47)"><div class="badge">APR<span>19</span></div></div><h3>Überschrift</h3><p>Lorem ipsum dolor sit amet, consetetur sadipscing elitr, sed diam nonumy...</p><span class="more">WEITER LESEN</span></article>
<article class="abs news" style="left:813px"><div class="img" role="img" aria-label="Visualisierung: moderne Wohnküche mit Essbereich" style="background:linear-gradient(90deg,#4b4440,#b8b2aa 50%,#d9d6d0)"><div class="badge">APR<span>19</span></div></div><h3>Überschrift</h3><p>Lorem ipsum dolor sit amet, consetetur sadipscing elitr, sed diam nonumy...</p><span class="more">WEITER LESEN</span></article>

<section class="abs contact"></section>
<div class="abs intro">
  <div class="kicker" style="font-size:16px;line-height:1.3">HABEN WIR IHR INTERESSE GEWECKT?<br>Dann treten Sie mit uns in Kontakt</div>
  <p>Wenn Sie Frage haben, ein Angebot oder einen Termin wünschen kontaktieren Sie uns.</p>
</div>
<div class="abs brand-small"><span class="sq"></span>WG Lindenhof eG</div>
<div class="abs addr">
  <div><svg width="12" height="15" viewBox="0 0 12 15"><path d="M6 0a5.5 5.5 0 0 0-5.5 5.5C.5 9.5 6 15 6 15s5.5-5.5 5.5-9.5A5.5 5.5 0 0 0 6 0zm0 7.5a2 2 0 1 1 0-4 2 2 0 0 1 0 4z" fill="#2e8a35"/></svg><span>Musterstraße 8,<br>09000 Musterstadt</span></div>
  <div><svg width="12" height="15" viewBox="0 0 12 15"><rect x="2" y="0.5" width="8" height="14" rx="1.5" fill="none" stroke="#2e8a35" stroke-width="1.5"/></svg><span>Tel. (01234) 56789<br>Fax (01234) 98765</span></div>
  <div><svg width="13" height="13" viewBox="0 0 13 13"><circle cx="6.5" cy="6.5" r="6" fill="#2e8a35"/><circle cx="6.5" cy="6.5" r="2.2" fill="#fff"/></svg><span>info@wg-lindenhof.example</span></div>
</div>
<div class="abs hours">
  <div class="h"><svg width="13" height="13" viewBox="0 0 13 13"><circle cx="6.5" cy="6.5" r="5.8" fill="none" stroke="#2e8a35" stroke-width="1.4"/><path d="M6.5 3v3.5H9" stroke="#2e8a35" stroke-width="1.4" fill="none"/></svg>Sprechzeiten</div>
  <div>Dienstag&nbsp;&nbsp;&nbsp;&nbsp;&nbsp;&nbsp;&nbsp;09:00 - 12:00 Uhr<br>Donnerstag&nbsp;&nbsp;13:00 - 16:00 Uhr</div>
</div>
<form class="abs form">
  <h2>KONTAKT</h2>
  <div class="field"><label>&#128100; Ihr Name*</label><div class="input"></div></div>
  <div class="field"><label>&#9742; Telefonnummer*</label><div class="input"></div></div>
  <div class="field"><label>&#128100; Ihr Anliegen*</label><div class="input"></div></div>
  <p class="note">Die mit * gekennzeichneten Felder sind Pflichtfelder.<br>Ihre Daten werden vertraulich behandelt.</p>
</form>
<span class="abs btn send">AB DIE POST</span>

<footer class="abs footer">
  <div class="links"><b>STARTSEITE</b> &nbsp;|&nbsp; ÜBER UNS &nbsp;&nbsp;|&nbsp;&nbsp; AKTUELLE MIETANGEBOTE &nbsp;&nbsp;|&nbsp;&nbsp; NEWS &nbsp;|&nbsp; OBJEKTSTANDORTE &nbsp;&nbsp;|&nbsp;&nbsp; NOTDIENST &nbsp;&nbsp;|&nbsp;&nbsp; KONTAKT</div>
  <div class="copy">© Unternehmensname 2019. All rights reserved.</div>
</footer>
</body>
</html>
```